Business Card & Logo Design for a communications based company

I am looking for a business card and logo design for a communications based company.. We specialize in Fiber Optics
I have an image i would like to use towards the logo which i have uploaded. (Use of the image is totally up to you the designers)
Background color - Blue OR Black. (thats just my preference..Use of those colors are totally up to the designer)
Text -
Company Name - Orbivane Communications LTD
Name - Kelvin Persadsingh
Contact Number - (868) 555-0172
Adress - Trincity
Company Motto - Stay Connected !
Services Offered
Fiber Optic Solutions
Full Networking Solutions
IP Surveillance Systems
Access Control Systems
Alarms
Communications
Text -
Name - Kelvin Persadsingh
Adress - Trincity
Services Offered
Fiber Optic Solutions
Full Networking Solutions
IP Surveillance Systems
Access Control Systems
Alarms

```html
<!DOCTYPE html>
<html lang="en">
<head>
<meta charset="utf-8">
<title>Orbivane Communications LTD — Business Card</title>
<link rel="stylesheet" href="https://fonts.googleapis.com/css2?family=Arimo:ital,wght@0,400;0,700;1,400;1,700&display=swap">
<style>
  :root {
    --stage-glow: #b3005f;
    --stage-mid: #5a0535;
    --stage-dark: #16000d;
    --card-black: #000000;
    --card-white: #ffffff;
    --accent-blue: #2f9ad8;
    --brand-blue: #1b8fe0;
    --ink-navy: #1a4f7e;
    --ink-deep: #0d3f86;
    --band-dark: #0a3d8f;
    --band-light: #e6eef8;
    --globe-light: #5fb4f0;
    --globe-mid: #2a7fd0;
    --globe-deep: #16529a;
  }
  html, body {
    margin: 0;
    padding: 0;
    width: 1200px;
    height: 1200px;
    overflow: hidden;
  }
  body {
    position: relative;
    font-family: "Arimo", Arial, sans-serif;
    background: radial-gradient(circle at 50% 45%, var(--stage-glow) 0%, var(--stage-mid) 45%, var(--stage-dark) 100%);
  }
  .card {
    position: absolute;
    border-radius: 16px;
    overflow: hidden;
  }
  .side-tab {
    position: absolute;
    width: 26px;
    border-radius: 12px;
  }

  /* Front */
  .card-front {
    left: 50px; top: 56px;
    width: 820px; height: 476px;
    background: var(--card-black);
    box-shadow: 0 2px 6px rgba(0,0,0,.5);
  }
  .card-front .side-tab { top: 64px; height: 330px; background: var(--accent-blue); }
  .card-front .tab-left { left: -6px; }
  .card-front .tab-right { right: -6px; }
  .faint-globe {
    position: absolute;
    left: -40px; top: 30px;
    width: 330px; height: 330px;
    border-radius: 50%;
    background: radial-gradient(circle closest-side, rgba(55,80,115,.35) 0%, rgba(30,42,60,.22) 70%, rgba(0,0,0,0) 100%);
  }
  .hero-art {
    position: absolute;
    left: 246px; top: 28px;
    width: 220px; height: 220px;
    border-radius: 50%;
    background: radial-gradient(circle at 40% 38%, var(--globe-light) 0%, var(--globe-mid) 45%, var(--globe-deep) 100%);
  }
  .company-name {
    position: absolute;
    left: 0; right: 0; top: 318px;
    margin: 0;
    text-align: center;
    font-size: 47px;
    font-weight: 700;
    color: var(--brand-blue);
  }
  .motto {
    position: absolute;
    left: 0; right: 0; top: 396px;
    margin: 0;
    text-align: center;
    font-size: 22px;
    font-weight: 400;
    color: var(--accent-blue);
    letter-spacing: .5px;
  }

  /* Back */
  .card-back {
    left: 240px; top: 636px;
    width: 856px; height: 484px;
    background: var(--card-white);
    box-shadow: 0 2px 6px rgba(0,0,0,.4);
  }
  .card-back .side-tab { top: 60px; height: 360px; background: var(--card-black); }
  .card-back .tab-left { left: -6px; }
  .card-back .tab-right { right: -6px; }
  .mini-art {
    position: absolute;
    left: 116px; top: 60px;
    width: 128px; height: 128px;
    border-radius: 50%;
    background: radial-gradient(circle at 40% 38%, var(--globe-light) 0%, var(--globe-mid) 45%, var(--globe-deep) 100%);
  }
  .holder-name {
    position: absolute;
    left: 328px; top: 100px;
    margin: 0;
    font-size: 34px;
    font-weight: 400;
    color: var(--ink-navy);
  }
  .contact-line {
    position: absolute;
    left: 94px; top: 262px;
    margin: 0;
    font-size: 26px;
    font-weight: 400;
    color: var(--ink-navy);
    white-space: pre;
  }
  .services {
    position: absolute;
    left: 66px; top: 328px;
    margin: 0;
    font-size: 20px;
    font-style: italic;
    color: var(--ink-deep);
    line-height: 26px;
    white-space: nowrap;
  }
  .services .indent { padding-left: 104px; display: block; }
  .base-band {
    position: absolute;
    left: 0; right: 0; top: 424px;
    height: 20px;
    background: linear-gradient(90deg, var(--band-dark) 0%, #1f5fb0 40%, #9bb8dc 75%, var(--band-light) 100%);
  }
</style>
</head>
<body>
  <section class="card card-front">
    <div class="faint-globe" role="img" aria-label="Faint enlarged globe artwork in the background"></div>
    <div class="side-tab tab-left"></div>
    <div class="side-tab tab-right"></div>
    <div class="hero-art" role="img" aria-label="Globe wrapped in a fiber optic cable with glowing strands"></div>
    <h1 class="company-name">Orbivane Communications LTD</h1>
    <p class="motto">STAY CONNECTED</p>
  </section>

  <section class="card card-back">
    <div class="side-tab tab-left"></div>
    <div class="side-tab tab-right"></div>
    <div class="mini-art" role="img" aria-label="Small globe wrapped in a fiber optic cable"></div>
    <h2 class="holder-name">Kelvin Persadsingh</h2>
    <p class="contact-line">Phone: (868) 555-0172    Address: Trincity Company</p>
    <p class="services">We offer:-  fiber optic solutions, Full networking Solutions, IP Surveillance<span class="indent">Systems, Access Control, System Alarms.</span></p>
    <div class="base-band"></div>
  </section>
</body>
</html>
```